hi all

Im after a new age looking business card with my company logo on it

must include these details, I would like the PH and Email to be symbols

If the colours used for card could be kept within the colours used in logo that I have supplied that would be great, if another colour is to be used dark grey would be ok. no light bulbs etc thanks

Details below to be incorporated on card

Damian Holloway

Lic E871302

PH 0219647381

E info@brightvaleelectrical.example.nz

Domestic Commercial Industrial Electricians

```html
<!DOCTYPE html>
<html lang="en">
<head>
<meta charset="utf-8">
<title>Brightvale Electrical – Business Card</title>
<link href="https://fonts.googleapis.com/css2?family=Poppins:wght@400;500;600&display=swap" rel="stylesheet">
<style>
  :root {
    --stage: #a3a8a8;
    --paper: #ffffff;
    --ink: #333333;
    --brand-blue: #1a7abf;
    --charcoal: #2a2a2a;
    --white: #ffffff;
  }
  * { box-sizing: border-box; margin: 0; padding: 0; }
  html, body { width: 1200px; height: 1000px; overflow: hidden; }
  body {
    background: var(--stage);
    font-family: "Poppins", Arial, sans-serif;
    position: relative;
  }
  .card {
    position: absolute;
    left: 220px;
    width: 760px;
    height: 435px;
  }
  .card--front { top: 43px; background: var(--paper); }
  .card--back { top: 522px; background: var(--charcoal); }

  .brand-front {
    position: absolute;
    right: 37px;
    top: 92px;
    display: flex;
    align-items: center;
    gap: 8px;
    color: var(--brand-blue);
    font-weight: 600;
    line-height: 1;
  }
  .brand-front .brand-dot {
    width: 14px; height: 14px; border-radius: 50%;
    background: var(--brand-blue);
  }
  .brand-front .brand-words { display: flex; flex-direction: column; align-items: flex-end; }
  .brand-front .brand-main { font-size: 24px; letter-spacing: 1px; }
  .brand-front .brand-sub { font-size: 10px; letter-spacing: 2px; margin-top: 4px; }

  .holder { position: absolute; left: 27px; top: 172px; }
  .holder-name {
    font-size: 34px; font-weight: 500; color: var(--brand-blue);
    line-height: 1.1; letter-spacing: 0.2px;
  }
  .holder-role { font-size: 18px; color: var(--ink); margin-top: 2px; }

  .divider {
    position: absolute; left: 0; right: 0; top: 257px;
    height: 3px; background: var(--brand-blue);
  }

  .address {
    position: absolute; left: 27px; top: 291px;
    font-size: 18px; color: var(--ink); line-height: 24px; font-style: normal;
  }

  .services {
    position: absolute; left: 27px; bottom: 28px;
    font-size: 14px; color: var(--brand-blue); letter-spacing: 0.5px;
  }

  .contacts {
    position: absolute; right: 27px; top: 276px;
    list-style: none; font-size: 18px; color: var(--ink);
  }
  .contacts li {
    display: flex; align-items: center; justify-content: flex-end;
    gap: 10px; height: 29px;
  }
  .contacts svg { width: 18px; height: 18px; stroke: var(--brand-blue); fill: none; stroke-width: 1.5; }
  .contacts .licence { font-size: 15px; }
  .contacts .licence .tag { color: var(--brand-blue); font-weight: 500; margin-right: 14px; }

  .brand-back {
    position: absolute; left: 0; right: 0; top: 222px;
    display: flex; justify-content: center;
  }
  .brand-back .brand-words {
    display: flex; flex-direction: column; align-items: flex-end;
    color: var(--white); font-weight: 600; line-height: 1;
  }
  .brand-back .brand-main { font-size: 40px; letter-spacing: 2px; }
  .brand-back .brand-sub { font-size: 13px; letter-spacing: 3px; margin-top: 6px; }
</style>
</head>
<body>
  <section class="card card--front">
    <div class="brand-front">
      <span class="brand-dot"></span>
      <div class="brand-words">
        <span class="brand-main">BRIGHTVALE</span>
        <span class="brand-sub">ELECTRICAL</span>
      </div>
    </div>

    <div class="holder">
      <h1 class="holder-name">ROWAN ELLERY</h1>
      <p class="holder-role">Director/CEO</p>
    </div>

    <div class="divider"></div>

    <address class="address">
      48 Harrow Rd. Unit<br>B, Kestrel Bay, Ontaria 40112
    </address>

    <ul class="contacts">
      <li>(555) 014-2290
        <svg viewBox="0 0 24 24" aria-hidden="true"><path d="M6 3l3 1 1 4-2 2c1 2 3 4 5 5l2-2 4 1 1 3-2 3C10 20 4 14 3 6z"/></svg>
      </li>
      <li>yourmail@mailbox.example
        <svg viewBox="0 0 24 24" aria-hidden="true"><rect x="3" y="6" width="18" height="12"/><path d="M3 6l9 7 9-7M3 18l7-6M21 18l-7-6"/></svg>
      </li>
      <li class="licence"><span><span class="tag">Lic</span>E871302</span></li>
    </ul>

    <p class="services">Domestic · Commercial · Industrial Electricians</p>
  </section>

  <section class="card card--back">
    <div class="brand-back">
      <div class="brand-words">
        <span class="brand-main">BRIGHTVALE</span>
        <span class="brand-sub">ELECTRICAL</span>
      </div>
    </div>
  </section>
</body>
</html>
```